Create a professional, eye-catching business card design that reflects the values and services of Brookfern Veterinary Hospital. we provide veterinary services and the business card should be a memorable representation of the clinic and align with its branding and mission. our tag line is "Life Long Companions, Lifelong Care"
Use clean, modern typography. Prioritize readability and professionalism. We would like to see designs that use the color blue, as in the logo example. the final design should communicate professionalism and care, with attention to detail.

```html
<!DOCTYPE html>
<html lang="en">
<head>
<meta charset="utf-8">
<title>Brookfern Veterinary Hospital — Business Card</title>
<link href="https://fonts.googleapis.com/css2?family=Montserrat:wght@400;500;700;800&display=swap" rel="stylesheet">
<style>
  :root {
    --navy: #1e3160;
    --paper: #ffffff;
    --backdrop: #f6f6f6;
  }
  * { margin: 0; padding: 0; box-sizing: border-box; }
  html, body {
    width: 1200px; height: 1200px; overflow: hidden;
    background: var(--backdrop);
    font-family: "Montserrat", Arial, sans-serif;
  }
  .card {
    position: absolute; left: 285px; width: 630px; height: 360px;
    overflow: hidden;
  }
  .card--front { top: 213px; background: var(--paper); color: var(--navy); --ink: var(--navy); }
  .card--back { top: 627px; background: var(--navy); color: var(--paper); --ink: var(--paper); }
  .frame { position: absolute; inset: 0; width: 630px; height: 360px; }
  .ornament {
    position: absolute; width: 14px; height: 14px; border-radius: 50%;
    background: var(--ink); opacity: .85;
  }
  .holder { position: absolute; left: 93px; top: 164px; }
  .holder__name { font-weight: 700; font-size: 17.5px; letter-spacing: .3px; line-height: 1; }
  .holder__role { font-size: 9.5px; font-weight: 400; margin-top: 3px; letter-spacing: .3px; }
  .contacts { position: absolute; left: 93px; top: 203px; list-style: none; }
  .contacts li { display: flex; align-items: center; height: 19px; margin-bottom: 9px; font-size: 11.5px; font-weight: 500; }
  .contacts .icon {
    width: 19px; height: 19px; border-radius: 50%; background: var(--navy);
    display: flex; align-items: center; justify-content: center; margin-right: 10px; flex: none;
  }
  .brand { position: absolute; text-align: center; font-weight: 800; color: var(--ink); line-height: 1; }
  .brand__mark { display: block; margin: 0 auto 10px; border: 2px solid var(--ink); border-radius: 50%; }
  .brand__name { display: block; }
  .brand__sub { display: block; }
  .card--front .brand { left: 355px; top: 98px; width: 200px; }
  .card--front .brand__mark { width: 110px; height: 110px; }
  .card--front .brand__name { font-size: 30px; letter-spacing: .5px; }
  .card--front .brand__sub { font-size: 11.6px; margin-top: 3px; letter-spacing: .4px; }
  .card--back .brand { left: 195px; top: 86px; width: 240px; }
  .card--back .brand__mark { width: 124px; height: 124px; }
  .card--back .brand__name { font-size: 37px; letter-spacing: .5px; }
  .card--back .brand__sub { font-size: 14.2px; margin-top: 4px; letter-spacing: .4px; }
</style>
</head>
<body>

<section class="card card--front">
  <svg class="frame" viewBox="0 0 630 360" aria-hidden="true">
    <g fill="none" stroke="#1e3160">
      <rect x="9.5" y="9.5" width="611" height="341" stroke-width="1.6"/>
      <line x1="66" y1="19" x2="564" y2="19" stroke-width="1.2"/>
      <line x1="66" y1="22" x2="564" y2="22" stroke-width="1.2"/>
      <line x1="66" y1="338" x2="564" y2="338" stroke-width="1.2"/>
      <line x1="66" y1="341" x2="564" y2="341" stroke-width="1.2"/>
      <line x1="18" y1="70" x2="18" y2="290" stroke-width="1.2"/>
      <line x1="21" y1="70" x2="21" y2="290" stroke-width="1.2"/>
      <line x1="609" y1="70" x2="609" y2="290" stroke-width="1.2"/>
      <line x1="612" y1="70" x2="612" y2="290" stroke-width="1.2"/>
    </g>
    <g fill="#1e3160">
      <polygon points="21,21 41,20 40,40 22,40"/>
      <polygon points="589,20 609,21 608,40 590,40"/>
      <polygon points="22,320 40,320 41,340 21,339"/>
      <polygon points="590,320 608,320 609,339 589,340"/>
    </g>
  </svg>
  <span class="ornament" role="img" aria-label="Scroll ornament" style="left:52px;top:20px"></span>
  <span class="ornament" role="img" aria-label="Scroll ornament" style="left:564px;top:20px"></span>
  <span class="ornament" role="img" aria-label="Scroll ornament" style="left:52px;top:326px"></span>
  <span class="ornament" role="img" aria-label="Scroll ornament" style="left:564px;top:326px"></span>
  <span class="ornament" role="img" aria-label="Scroll ornament" style="left:18px;top:54px"></span>
  <span class="ornament" role="img" aria-label="Scroll ornament" style="left:598px;top:54px"></span>
  <span class="ornament" role="img" aria-label="Scroll ornament" style="left:18px;top:292px"></span>
  <span class="ornament" role="img" aria-label="Scroll ornament" style="left:598px;top:292px"></span>

  <div class="holder">
    <p class="holder__name">YOUR NAME</p>
    <p class="holder__role">CEO</p>
  </div>
  <ul class="contacts">
    <li><span class="icon"><svg width="10" height="10" viewBox="0 0 24 24" aria-hidden="true"><path fill="#fff" d="M6.6 10.8a15 15 0 0 0 6.6 6.6l2.2-2.2a1 1 0 0 1 1-.25 11.4 11.4 0 0 0 3.6.57 1 1 0 0 1 1 1V20a1 1 0 0 1-1 1A17 17 0 0 1 3 4a1 1 0 0 1 1-1h3.5a1 1 0 0 1 1 1c0 1.25.2 2.45.57 3.57a1 1 0 0 1-.25 1z"/></svg></span>( Phone ) 000-000-0001</li>
    <li><span class="icon"><svg width="10" height="8" viewBox="0 0 20 14" aria-hidden="true"><rect x="1" y="1" width="18" height="12" fill="none" stroke="#fff" stroke-width="1.6"/><path d="M1 1l9 7 9-7" fill="none" stroke="#fff" stroke-width="1.6"/></svg></span>info@yourname.com</li>
    <li><span class="icon"><svg width="11" height="11" viewBox="0 0 20 20" aria-hidden="true"><circle cx="10" cy="10" r="8" fill="none" stroke="#fff" stroke-width="1.6"/><path d="M2 10h16M10 2c3 3 3 13 0 16M10 2c-3 3-3 13 0 16" fill="none" stroke="#fff" stroke-width="1.2"/></svg></span>www.yourwebsite.com</li>
  </ul>

  <div class="brand">
    <span class="brand__mark"></span>
    <span class="brand__name">BROOKFERN</span>
    <span class="brand__sub">VETERINARY HOSPITAL</span>
  </div>
</section>

<section class="card card--back">
  <svg class="frame" viewBox="0 0 630 360" aria-hidden="true">
    <g fill="none" stroke="#ffffff">
      <rect x="9.5" y="9.5" width="611" height="341" stroke-width="1.6"/>
      <line x1="66" y1="19" x2="564" y2="19" stroke-width="1.2"/>
      <line x1="66" y1="22" x2="564" y2="22" stroke-width="1.2"/>
      <line x1="66" y1="338" x2="564" y2="338" stroke-width="1.2"/>
      <line x1="66" y1="341" x2="564" y2="341" stroke-width="1.2"/>
      <line x1="18" y1="70" x2="18" y2="290" stroke-width="1.2"/>
      <line x1="21" y1="70" x2="21" y2="290" stroke-width="1.2"/>
      <line x1="609" y1="70" x2="609" y2="290" stroke-width="1.2"/>
      <line x1="612" y1="70" x2="612" y2="290" stroke-width="1.2"/>
    </g>
    <g fill="#ffffff">
      <polygon points="21,21 41,20 40,40 22,40"/>
      <polygon points="589,20 609,21 608,40 590,40"/>
      <polygon points="22,320 40,320 41,340 21,339"/>
      <polygon points="590,320 608,320 609,339 589,340"/>
    </g>
  </svg>
  <span class="ornament" role="img" aria-label="Scroll ornament" style="left:52px;top:20px"></span>
  <span class="ornament" role="img" aria-label="Scroll ornament" style="left:564px;top:20px"></span>
  <span class="ornament" role="img" aria-label="Scroll ornament" style="left:52px;top:326px"></span>
  <span class="ornament" role="img" aria-label="Scroll ornament" style="left:564px;top:326px"></span>
  <span class="ornament" role="img" aria-label="Scroll ornament" style="left:18px;top:54px"></span>
  <span class="ornament" role="img" aria-label="Scroll ornament" style="left:598px;top:54px"></span>
  <span class="ornament" role="img" aria-label="Scroll ornament" style="left:18px;top:292px"></span>
  <span class="ornament" role="img" aria-label="Scroll ornament" style="left:598px;top:292px"></span>

  <div class="brand">
    <span class="brand__mark"></span>
    <span class="brand__name">BROOKFERN</span>
    <span class="brand__sub">VETERINARY HOSPITAL</span>
  </div>
</section>

</body>
</html>
```